Design for candybags for heapsweets.

I need 3 designs for 3 candybags (3 flavors). Or the same design but different colours
- licorice (black)
- sour (green/yellow ish)
- mix (purple from our website #7F1150)
I want our logo to be in the bags (see nordicpickmix.com) there has to be space in the back of the bag for the bar code and nutritionlist. There has to be a transparent part in the front of the bag, so that you can see the candy in the bag. The size of the bags is 420×594 mm. I want a childish style but at the same time it has to be appealing. I am open minded so if you have a good idea Please let know.

Industry/Entity Type

Food Store

Colors

Designer to choose colors to be used in the design.

Requirements
Must have
• Our logo (www.nordicpickmix.com)
• Space in the back for the nutritionlist and Bar-Code.
• Transparent part at the front side (or back and front) for the customers to be able to see the candy inside.
• The design artwork format has to be in: PSD, AI or CDR.

```html
<!DOCTYPE html>
<html lang="en">
<head>
<meta charset="utf-8">
<title>Nordic Pickmix – Candy Bag Range</title>
<link rel="stylesheet" href="https://fonts.googleapis.com/css2?family=Amatic+SC:wght@700&family=Nunito:wght@400;700;800&display=swap">
<style>
  :root {
    --backdrop: #a9bfcc;
    --cream: #eee8da;
    --title-cream: #f4e7b9;
    --licorice: #2b2a2c;
    --mix: #b3227f;
    --sour: #9cad2c;
    --ink: #2a2a2a;
    --white: #ffffff;
    --art-licorice: #8a5a3c;
    --art-mix: #c7714a;
    --art-sour: #f1d733;
    --window-licorice: linear-gradient(160deg, #3a3434, #e9a6b4 45%, #f2d64a 70%, #2a2627);
    --window-mix: linear-gradient(160deg, #5a2b2b, #d23b34 40%, #e4a338 65%, #3b2a5a);
    --window-sour: linear-gradient(160deg, #d8c64a, #e0503e 40%, #7fb246 65%, #8c3b7a);
  }
  * { box-sizing: border-box; margin: 0; padding: 0; }
  html, body { width: 1200px; height: 800px; overflow: hidden; }
  body { background: var(--backdrop); font-family: "Nunito", sans-serif; }
  .canvas { position: relative; width: 1200px; height: 800px; }

  .bag { position: absolute; width: 224px; overflow: hidden; border-radius: 4px;
         background: var(--cream); box-shadow: 0 3px 8px rgba(0,0,0,.18); }
  .bag::before, .bag::after { content: ""; position: absolute; left: 0; right: 0; height: 7px;
         background: repeating-linear-gradient(90deg, rgba(0,0,0,.06) 0 2px, transparent 2px 4px); z-index: 5; }
  .bag::before { top: 0; } .bag::after { bottom: 0; }

  .front { top: 52px; height: 336px; }
  .back { top: 446px; height: 326px; width: 222px; }
  .col-1 { left: 226px; } .col-2 { left: 488px; } .col-3 { left: 756px; }

  .licorice { --flavour: var(--licorice); --art: var(--art-licorice); --window: var(--window-licorice); --head: var(--title-cream); }
  .mix { --flavour: var(--mix); --art: var(--art-mix); --window: var(--window-mix); --head: var(--white); }
  .sour { --flavour: var(--sour); --art: var(--art-sour); --window: var(--window-sour); --head: var(--white); }

  .logo { display: flex; align-items: center; gap: 4px; font-weight: 800; letter-spacing: .03em; white-space: nowrap; }
  .logo .dot { width: 10px; height: 10px; border-radius: 50%; background: currentColor; flex: none; }
  .title { font-family: "Amatic SC", cursive; color: var(--head); text-align: center; line-height: .88; }
  .subtitle { display: block; font-family: "Amatic SC", cursive; color: var(--head); text-align: center;
              font-size: 15px; letter-spacing: .18em; }

  /* Front */
  .band { position: absolute; top: 0; left: 26%; width: 64%; height: 48%; background: var(--flavour);
          display: flex; flex-direction: column; align-items: center; padding-top: 20px; z-index: 2; }
  .band .logo { font-size: 9px; color: var(--title-cream); }
  .front .title { font-size: 42px; margin-top: 14px; }
  .art { position: absolute; left: 10%; width: 82%; top: 40%; bottom: 0; background: var(--art);
         border-radius: 40% 40% 0 0 / 22% 22% 0 0; z-index: 1; }
  .window { position: absolute; left: 22%; width: 58%; top: 68%; bottom: 0; background: var(--window);
            border-radius: 12px 12px 0 0; z-index: 3; opacity: .92; }
  .side-note { position: absolute; right: 4px; top: 8px; writing-mode: vertical-rl; font-size: 5.5px;
               letter-spacing: .08em; color: var(--ink); font-weight: 700; z-index: 4; }
  .net { position: absolute; right: 8px; bottom: 24px; font-size: 7px; font-weight: 800;
         letter-spacing: .05em; color: var(--ink); z-index: 4; }

  /* Back */
  .back-panel { position: absolute; left: 0; right: 0; top: 0; height: 270px; background: var(--flavour); color: var(--white); }
  .back .title { position: absolute; left: 0; right: 0; top: 28px; font-size: 42px; }
  .back .subtitle { position: absolute; left: 0; right: 0; top: 72px; }
  .blurb { position: absolute; left: 14px; right: 14px; top: 100px; font-size: 7.5px; line-height: 11px;
           text-align: center; font-weight: 700; }
  .licorice .blurb { top: 104px; }
  .back .logo { position: absolute; left: 16px; top: 186px; font-size: 9px; color: var(--white); }
  .claim { position: absolute; left: 22px; top: 236px; font-family: "Amatic SC", cursive; font-size: 19px; color: var(--white); }
  .nutrition { position: absolute; left: 118px; top: 150px; width: 84px; height: 84px; background: var(--white);
               color: var(--ink); border-radius: 4px; padding: 6px 7px; font-size: 4.6px; }
  .nutrition h3 { font-size: 4.6px; text-align: center; font-weight: 800; margin-bottom: 5px; }
  .nutrition table { width: 100%; border-collapse: collapse; }
  .nutrition td { border-bottom: .5px solid #999; padding: 1px 0; }
  .nutrition td:last-child { text-align: right; }
  .nutrition p { margin-top: 8px; text-align: center; }
  .ingredients { position: absolute; left: 116px; top: 240px; width: 92px; font-size: 4.2px; line-height: 1.35; color: var(--white); }
  .packed { position: absolute; left: 12px; top: 282px; font-size: 4.2px; line-height: 1.4; color: var(--ink); }
  .packed strong { font-weight: 800; }
  .net-weight { position: absolute; left: 12px; top: 304px; font-size: 9px; font-weight: 800; color: var(--ink); }
  .code-space { position: absolute; left: 136px; top: 278px; width: 74px; height: 28px; background: var(--white); }
  .exp { position: absolute; left: 150px; top: 310px; font-size: 4.2px; font-weight: 700; color: var(--ink); }
</style>
</head>
<body>
<main class="canvas">

  <article class="bag front licorice col-1">
    <div class="band">
      <div class="logo"><span class="dot"></span>Nordic Pickmix</div>
      <h2 class="title">Licorice</h2>
      <span class="subtitle">All sorts</span>
    </div>
    <div class="art" role="img" aria-label="Illustrated brown character holding the candy"></div>
    <div class="window" role="img" aria-label="Clear window showing licorice allsorts inside the bag"></div>
    <p class="side-note">NO ADDED ARTIFICIAL COLOUR OR FLAVOR</p>
  </article>

  <article class="bag front mix col-2">
    <div class="band">
      <div class="logo"><span class="dot"></span>Nordic Pickmix</div>
      <h2 class="title">Mix<br>Candy</h2>
    </div>
    <div class="art" role="img" aria-label="Illustrated bear character wearing a pink cap and blue hoodie"></div>
    <div class="window" role="img" aria-label="Clear window showing mixed wrapped candy inside the bag"></div>
    <p class="side-note">NO ADDED ARTIFICIAL COLOUR OR FLAVOR</p>
    <p class="net">NET 180G</p>
  </article>

  <article class="bag front sour col-3">
    <div class="band">
      <div class="logo"><span class="dot"></span>Nordic Pickmix</div>
      <h2 class="title">Sour<br>Candy</h2>
    </div>
    <div class="art" role="img" aria-label="Illustrated yellow bird character wearing a green hat"></div>
    <div class="window" role="img" aria-label="Clear window showing colourful sour candy inside the bag"></div>
    <p class="side-note">NO ADDED ARTIFICIAL COLOUR OR FLAVOR</p>
    <p class="net">NET 180G</p>
  </article>

  <article class="bag back licorice col-1">
    <div class="back-panel">
      <h2 class="title">Licorice</h2>
      <span class="subtitle">All sorts</span>
      <p class="blurb">Get all the allsorted licorice candy from Nordic Pickmix! delicious and healthy candy for you all! This is just text placement you can edit later with your own text</p>
      <div class="logo"><span class="dot"></span>Nordic Pickmix</div>
      <p class="claim">100% Swedish!</p>
      <div class="nutrition">
        <h3>NUTRITION FACT</h3>
        <table><tr><td>Fat</td><td>4%</td></tr><tr><td>Sugar</td><td>6%</td></tr><tr><td>Fiber</td><td>3%</td></tr><tr><td>Others</td><td>8%</td></tr></table>
        <p>% Value is based on diet calorie</p>
      </div>
      <p class="ingredients">INGREDIENTS : This is the place for your ingredients, food and candy details.</p>
    </div>
    <p class="packed"><strong>Packed and produced by:</strong><br>Nordic Pickmix Ltd<br>Harbour Street 4, Malmö<br>www.nordicpickmix.com</p>
    <p class="net-weight">Net 180g</p>
    <div class="code-space" aria-hidden="true"></div>
    <p class="exp">EXP. date : 21/01/2019</p>
  </article>

  <article class="bag back mix col-2">
    <div class="back-panel">
      <h2 class="title">Mix<br>Candy</h2>
      <p class="blurb">Get all the allsorted mix candy from Nordic Pickmix! delicious and healthy candy for you all! This is just text placement you can edit later with your own text</p>
      <div class="logo"><span class="dot"></span>Nordic Pickmix</div>
      <p class="claim">100% Swedish!</p>
      <div class="nutrition">
        <h3>NUTRITION FACT</h3>
        <table><tr><td>Fat</td><td>4%</td></tr><tr><td>Sugar</td><td>6%</td></tr><tr><td>Fiber</td><td>3%</td></tr><tr><td>Others</td><td>8%</td></tr></table>
        <p>% Value is based on diet calorie</p>
      </div>
      <p class="ingredients">INGREDIENTS : This is the place for your ingredients, food and candy details.</p>
    </div>
    <p class="packed"><strong>Packed and produced by:</strong><br>Nordic Pickmix Ltd<br>Harbour Street 4, Malmö<br>www.nordicpickmix.com</p>
    <p class="net-weight">Net 180g</p>
    <div class="code-space" aria-hidden="true"></div>
    <p class="exp">EXP. date : 21/01/2019</p>
  </article>

  <article class="bag back sour col-3">
    <div class="back-panel">
      <h2 class="title">Sour<br>Candy</h2>
      <p class="blurb">Get all the allsorted sour candy from Nordic Pickmix! delicious and healthy candy for you all! This is just text placement you can edit later with your own text</p>
      <div class="logo"><span class="dot"></span>Nordic Pickmix</div>
      <p class="claim">100% Swedish!</p>
      <div class="nutrition">
        <h3>NUTRITION FACT</h3>
        <table><tr><td>Fat</td><td>4%</td></tr><tr><td>Sugar</td><td>6%</td></tr><tr><td>Fiber</td><td>3%</td></tr><tr><td>Others</td><td>8%</td></tr></table>
        <p>% Value is based on diet calorie</p>
      </div>
      <p class="ingredients">INGREDIENTS : This is the place for your ingredients, food and candy details.</p>
    </div>
    <p class="packed"><strong>Packed and produced by:</strong><br>Nordic Pickmix Ltd<br>Harbour Street 4, Malmö<br>www.nordicpickmix.com</p>
    <p class="net-weight">Net 180g</p>
    <div class="code-space" aria-hidden="true"></div>
    <p class="exp">EXP. date : 21/01/2019</p>
  </article>

</main>
</body>
</html>
```